Alaska Law Firm Needs a Sticker Design

We need a design for stickers to put on already-printed brochures. We mail the brochures to potential clients so they can learn more about accident-induced injuries, insurance claims, legal representation, and our own law firm.

One of our lawyers wrote a book that provides a helpful overview of personal injury claims. We are offering this book for free to anyone who calls and requests it. Therefore, the sticker design should include one of the following phrases, or something very similar:
a) "Still have questions? Call and request our book-- for free!"
b) "Still have questions about auto accident claims? Call and request our book today."
c) "Still have questions about filing a claim? Call and request a free copy of our book."
d) "Still have questions? Call us today to request a free copy of our book, Clear Lanes Ahead."
e) "To learn more about automobile accidents and insurance, call today and request a free copy of our book."

The sticker should be approximately 3"x3" and may be a circle, square, rectangle, or ellipsis. The sticker will be placed on the back of the folder, which is light blue. We would like the sticker to match the color scheme of our website and the folder.

I will upload an image of the book cover as soon as I obtain it.

Industry/Entity Type

Law Firm

Font styles to use
Serif
Sans Serif

Requirements
Should not have
• Bright colors that aren't already used in the folder design. e.g. no bright orange, pink, chartreuse, turquoise, yellow, red.

```html
<!DOCTYPE html>
<html lang="en">
<head>
<meta charset="utf-8">
<title>Have Questions? Free Book Sticker</title>
<link rel="stylesheet" href="https://fonts.googleapis.com/css2?family=Fira+Sans+Condensed:wght@700&family=Fira+Sans+Extra+Condensed:wght@700&display=swap">
<style>
  :root {
    --navy: #0a2c6c;
    --sky: #95bfe6;
    --white: #ffffff;
    --backdrop: #f3f3f3;
    --star: #8bb8e3;
  }
  html, body {
    margin: 0;
    padding: 0;
    width: 1200px;
    height: 1200px;
    overflow: hidden;
    background: var(--backdrop);
  }
  .sticker {
    display: block;
    width: 1200px;
    height: 1200px;
  }
  .sticker-rim { fill: var(--navy); }
  .sticker-field { fill: var(--sky); }
  .offer-band { fill: var(--navy); }
  .band-star { fill: var(--star); }
  .headline {
    font-family: "Fira Sans Extra Condensed", "Arial Narrow", sans-serif;
    font-weight: 700;
    fill: var(--navy);
    text-anchor: middle;
  }
  .offer-line {
    font-family: "Fira Sans Condensed", "Arial Narrow", sans-serif;
    font-weight: 700;
    fill: var(--white);
    text-anchor: middle;
  }
  .phone-line {
    font-family: "Fira Sans Condensed", "Arial Narrow", sans-serif;
    font-weight: 700;
    fill: var(--white);
    font-size: 66px;
  }
</style>
</head>
<body>
<svg class="sticker" viewBox="0 0 1200 1200" xmlns="http://www.w3.org/2000/svg" aria-label="Have questions? Call and request our book for free! (555) 014 2288">
  <defs>
    <clipPath id="rim-clip">
      <ellipse cx="600" cy="600" rx="494" ry="356"/>
    </clipPath>
    <path id="phone-arc" d="M 260 858 Q 600 950 940 858" fill="none"/>
  </defs>

  <ellipse class="sticker-rim" cx="600" cy="600" rx="494" ry="356"/>
  <ellipse class="sticker-field" cx="600" cy="577" rx="432" ry="275"/>
  <rect class="offer-band" x="100" y="562" width="1000" height="117" clip-path="url(#rim-clip)"/>

  <text class="headline" x="600" y="427" font-size="106">HAVE</text>
  <text class="headline" x="600" y="534" font-size="128">QUESTIONS?</text>

  <polygon class="band-star" transform="translate(154 618)"
    points="0,-21 6,-7 21,-6 10,4 13,19 0,11 -13,19 -10,4 -21,-6 -6,-7"/>
  <text class="offer-line" x="600" y="643" font-size="80">Call and request our book</text>
  <polygon class="band-star" transform="translate(1046 618)"
    points="0,-21 6,-7 21,-6 10,4 13,19 0,11 -13,19 -10,4 -21,-6 -6,-7"/>

  <text class="headline" x="600" y="795" font-size="140">for FREE!</text>

  <text class="phone-line">
    <textPath href="#phone-arc" startOffset="50%" text-anchor="middle">- (555) 014 2288 -</textPath>
  </text>
</svg>
</body>
</html>
```